Branding for Velēra Cider a new Tasmanian cider company

We are a new Tasmanian cider business looking for a logo/label design to be used on our 330ml cider bottle labels and as a logo.
We want our cider label to pop and stand out from the rest.
As our cider is a Tasmanian product we would like it to appear as a premium product.
I have attached pictures of all of the other Tasmanian Cider labels to give an idea of what we are competing with NOT because we like the designs!!!

We are yet to start advertising our business so it is all an open slab, we have no starting point just a few ideas that have been listed below in the "Nice to Haves" section.

This brief has been updated as what we originally requested was too similar to other labels already in production so didn't give our product an edge.

The label size will be approx 80mm x 125mm

Target Market(s)

Craft cider market, bottle shops, boutique bars and restaurants

Font styles to use
Serif
Decorative
Script

Colors

Designer to choose colors to be used in the design.

Requirements
Must have
• The words
• "Velēra Cider" with the diacritic's over the o's
• "Tasmanian Made"
• or
• "Made in Tasmania"
• The Tasmanian part can be in all caps if it looks better
Nice to have
• All or some of the below incorporated into the label:
• Velēra was the goddess of fruit trees, gardens, and orchards.
• She watched over and protected fruit trees
• She was thought to be a wood nymph which are usually represented as beautiful, young girls.
• We would like our label to possibly incorporate the above.
• Maybe a wood nymph/goddess in an apple/pear orchard or against an apple/pear tree.
• Maybe no tree, just the nymph/goddess holding fruit.
• Maybe an apple/pear branch with a nympy/goddess under it.
• I have attached a few images from searchly of wood nymphs and fruit goddess' for inspiration. Not sure if realistic or animated would look best, but if animated, not cartoon like as we would like a premium look. Possibly similar to the attached Torvik Cider artwork
• We will have 3 types of cider; Apple, Pear and Apple & Strawberry so essentially 3 labels, maybe the apple tree could change to a pear tree and for the apple & strawberry cider maybe strawberries growing under the apple tree?
• All just ideas, we are open to :)
• If you think something else will suit the name, please feel free to submit it

```html
<!DOCTYPE html>
<html lang="en">
<head>
<meta charset="utf-8">
<title>Velēra Cider – Label Range</title>
<link href="https://fonts.googleapis.com/css2?family=Cormorant+Garamond:wght@500;600;700&display=swap" rel="stylesheet">
<style>
  :root {
    --canvas: #ffffff;
    --paper: #faf8f1;
    --ink: #1c1a17;
    --white: #ffffff;
    --apple-band: #a3ad33;
    --pear-band: #f09b20;
    --berry-band: #e55548;
    --apple-fruit: #f7c81c;
    --apple-fruit-deep: #e9b400;
    --pear-fruit: #eeac2c;
    --pear-fruit-deep: #d98e14;
    --green-apple: #c4c12e;
    --strawberry: #e0453c;
  }
  * { box-sizing: border-box; margin: 0; padding: 0; }
  html, body { width: 1200px; height: 665px; overflow: hidden; background: var(--canvas); }
  .range { position: relative; width: 1200px; height: 665px; }

  .label {
    position: absolute;
    top: 95px;
    width: 305px;
    height: 473px;
    background: var(--paper);
    box-shadow: 0 10px 34px rgba(0,0,0,0.16), 0 2px 6px rgba(0,0,0,0.06);
    font-family: "Cormorant Garamond", serif;
    color: var(--ink);
    text-align: center;
  }
  .label--apple { left: 96px; }
  .label--pear { left: 444px; }
  .label--berry { left: 803px; }

  .origin {
    position: absolute;
    top: 65px;
    left: 0;
    width: 100%;
    height: 42px;
    font-size: 17px;
    font-weight: 600;
    letter-spacing: 0.08em;
    line-height: 42px;
    white-space: nowrap;
  }
  .origin::before,
  .origin::after {
    content: "";
    position: absolute;
    left: 50%;
    width: 80px;
    margin-left: -40px;
    border-top: 1px solid var(--ink);
  }
  .origin::before { top: 0; }
  .origin::after { bottom: 0; }

  .fruit-art {
    position: absolute;
    left: 50px;
    width: 205px;
    top: 160px;
    height: 125px;
    border-radius: 100px 100px 0 0;
  }
  .label--apple .fruit-art { background: radial-gradient(ellipse at 50% 70%, var(--apple-fruit) 0%, var(--apple-fruit-deep) 100%); }
  .label--pear .fruit-art { background: radial-gradient(ellipse at 50% 70%, var(--pear-fruit) 0%, var(--pear-fruit-deep) 100%); }
  .label--berry .fruit-art { background: linear-gradient(90deg, var(--strawberry) 0%, var(--green-apple) 30%, var(--green-apple) 70%, var(--strawberry) 100%); }

  .flavour-band {
    position: absolute;
    top: 285px;
    left: 0;
    width: 100%;
    height: 50px;
    padding-bottom: 4px;
    display: flex;
    align-items: flex-end;
    justify-content: center;
    color: var(--white);
    font-size: 21px;
    font-weight: 600;
    letter-spacing: 0.04em;
    line-height: 1;
  }
  .label--apple .flavour-band { background: var(--apple-band); }
  .label--pear .flavour-band { background: var(--pear-band); }
  .label--berry .flavour-band { background: var(--berry-band); }

  .brand-name {
    position: absolute;
    top: 336px;
    left: 0;
    width: 100%;
    font-size: 44px;
    font-weight: 700;
    line-height: 40px;
    letter-spacing: 0.03em;
  }

  .volume {
    position: absolute;
    top: 428px;
    left: 0;
    width: 100%;
    font-weight: 700;
    font-size: 22px;
    line-height: 1;
  }
  .volume small { font-size: 16px; }
</style>
</head>
<body>
<main class="range">

  <section class="label label--apple">
    <p class="origin">MADE IN TASMANIA</p>
    <div class="fruit-art" role="img" aria-label="Illustration of yellow apples with green leaves"></div>
    <p class="flavour-band">APPLE</p>
    <h2 class="brand-name">VELĒRA<br>CIDER</h2>
    <p class="volume">330 <small>ml</small></p>
  </section>

  <section class="label label--pear">
    <p class="origin">MADE IN TASMANIA</p>
    <div class="fruit-art" role="img" aria-label="Illustration of golden pears with green leaves"></div>
    <p class="flavour-band">PEAR</p>
    <h2 class="brand-name">VELĒRA<br>CIDER</h2>
    <p class="volume">330 <small>ml</small></p>
  </section>

  <section class="label label--berry">
    <p class="origin">MADE IN TASMANIA</p>
    <div class="fruit-art" role="img" aria-label="Illustration of a green apple flanked by strawberries"></div>
    <p class="flavour-band">APPLE &amp; STRAWBERRY</p>
    <h2 class="brand-name">VELĒRA<br>CIDER</h2>
    <p class="volume">330 <small>ml</small></p>
  </section>

</main>
</body>
</html>
```